Crestline Lending Group Business Cards

We are looking to revamp the current business cards each of our locations uses. We are a lending company that specializes in personal loans, title loans, and tax services. We have locations in New Mexico, Texas, and Oklahoma.

We would like a cleaner, sleeker look while still highlighting what we offer. Title Loans, Personal Loans & Tax Services. We also want to include our referral fee somewhere on the card. We would like to see an English option as well as a Spanish option for the cards.

PLEASE NOTE: Some business cards do not include the employee's name but just the store's location, while others will include both.

These are double-sided business cards, and we would like to see proof if possible. I have included proofs of our current business cards for you to review below, as well as our company logo. Feel free to get creative with the logo, etc! Colors should match the logo; however, you do not need to use all of our logo colors if you don't want to.

```html
<!DOCTYPE html>
<html lang="en">
<head>
<meta charset="utf-8">
<title>Crestline Lending Group Business Card</title>
<link href="https://fonts.googleapis.com/css2?family=Anton&family=Francois+One&family=Montserrat:wght@400&display=swap" rel="stylesheet">
<style>
  :root {
    --green: #0f4f2c;
    --red: #b81c25;
    --white: #f4f4f2;
    --page: #ffffff;
  }
  * { box-sizing: border-box; margin: 0; padding: 0; }
  html, body { width: 1200px; height: 1200px; overflow: hidden; background: var(--page); }
  .sheet { position: relative; width: 1200px; height: 1200px; }
  .card {
    position: absolute; top: 450px; width: 520px; height: 290px;
    background: var(--white); overflow: hidden;
    box-shadow: 0 10px 30px rgba(0,0,0,0.22);
  }
  .card--front { left: 50px; }
  .card--back { left: 630px; }

  /* Front */
  .brand {
    position: absolute; left: 0; top: 0; width: 260px; height: 190px;
    display: flex; flex-direction: column; align-items: center; justify-content: center; gap: 8px;
  }
  .brand__mark { width: 22px; height: 22px; border-radius: 50%; background: var(--red); }
  .brand__name {
    font-family: "Francois One", sans-serif; color: var(--green);
    font-size: 27px; line-height: 1.05; text-align: center;
  }
  .brand__web { font-family: "Montserrat", sans-serif; color: var(--green); font-size: 11px; }
  .contact {
    position: absolute; left: 260px; top: 0; width: 260px; height: 190px;
    background: var(--green); color: #fff; padding: 38px 0 0 54px;
  }
  .contact__name { font-family: "Francois One", sans-serif; font-size: 23px; line-height: 1.1; }
  .contact__title { font-family: "Montserrat", sans-serif; font-size: 11.5px; letter-spacing: 0.3px; margin-bottom: 14px; }
  .contact__phone { font-family: "Francois One", sans-serif; font-size: 23px; line-height: 1.1; }
  .contact__email { font-family: "Francois One", sans-serif; font-size: 14px; }
  .services {
    position: absolute; left: 0; top: 190px; width: 520px; height: 48px;
    background: var(--red); display: flex; align-items: center; justify-content: space-evenly;
    font-family: "Francois One", sans-serif; color: #fff; font-size: 18px; letter-spacing: 0.3px;
  }
  .services__item::before {
    content: ""; display: inline-block; width: 10px; height: 10px; border-radius: 50%;
    background: var(--green); margin-right: 7px; vertical-align: 2px;
  }
  .address {
    position: absolute; left: 0; top: 238px; width: 520px; height: 42px;
    display: flex; align-items: center; justify-content: center;
    font-family: "Francois One", sans-serif; color: var(--green); font-size: 21px;
  }
  .card__foot { position: absolute; left: 0; bottom: 0; width: 520px; height: 10px; background: var(--green); }

  /* Back */
  .referral {
    position: absolute; left: 0; top: 0; width: 520px; height: 80px;
    background: var(--red); display: flex; align-items: center; padding-left: 30px; gap: 18px;
  }
  .referral__text { font-family: "Francois One", sans-serif; color: #fff; font-size: 44px; line-height: 1; }
  .offer {
    position: absolute; left: 0; top: 80px; width: 520px; height: 166px;
    display: flex; align-items: center; justify-content: center; gap: 10px;
    font-family: "Anton", sans-serif; color: var(--green);
  }
  .offer__big { font-size: 124px; line-height: 1; }
  .offer__stack {
    display: flex; flex-direction: column; align-items: center;
    color: var(--red); font-size: 50px; line-height: 0.98;
  }
  .card__band { position: absolute; left: 0; bottom: 0; width: 520px; height: 44px; background: var(--green); }
</style>
</head>
<body>
<main class="sheet">
  <section class="card card--front" aria-label="Business card front">
    <div class="brand">
      <span class="brand__mark"></span>
      <span class="brand__name">Crestline Lending Group</span>
      <span class="brand__web">www.crestlinelending.com</span>
    </div>
    <div class="contact">
      <p class="contact__name">Elena Ruiz</p>
      <p class="contact__title">BRANCH MANAGER</p>
      <p class="contact__phone">(575) 240-3316</p>
      <p class="contact__email">eruiz@crestlinelending.com</p>
    </div>
    <div class="services">
      <span class="services__item">TITLE LOANS</span>
      <span class="services__item">PERSONAL LOANS</span>
      <span class="services__item">TAX SERVICES</span>
    </div>
    <p class="address">48 Cedar Lane, Unit C, Rivertown, Texas 75012</p>
    <div class="card__foot"></div>
  </section>

  <section class="card card--back" aria-label="Business card back">
    <div class="referral">
      <span class="referral__text">Refer a Friend</span>
      <svg class="referral__arrow" width="150" height="30" viewBox="0 0 150 30" aria-hidden="true">
        <rect x="0" y="12" width="128" height="6" fill="#fff"/>
        <polygon points="124,3 150,15 124,27" fill="#fff"/>
      </svg>
    </div>
    <div class="offer">
      <span class="offer__big">GET</span>
      <span class="offer__stack"><span>UP</span><span>TO</span></span>
      <span class="offer__big">$100</span>
    </div>
    <div class="card__band"></div>
  </section>
</main>
</body>
</html>
```